Flyer for Choir Christmas Concert

Need colorful flyer for Christmas Choir Concert.

Requirements
Should not have
• I don't like musical symbols incorporated into the design.

```html
<!DOCTYPE html>
<html lang="en">
<head>
<meta charset="utf-8">
<title>Love &amp; Joy – Christmas Choir Concert</title>
<link rel="stylesheet" href="https://fonts.googleapis.com/css2?family=Stardos+Stencil:wght@700&family=Lora:wght@400;600;700&display=swap">
<style>
  :root {
    --red-deep: #a3070f;
    --red-mid: #d0101b;
    --red-bright: #e8242a;
    --white: #ffffff;
    --gold: #e6b53c;
    --gold-dark: #9c6a12;
    --purple: #4b2a6e;
    --ink: #3a2a48;
  }
  * { margin: 0; padding: 0; box-sizing: border-box; }
  html, body { width: 849px; height: 1200px; overflow: hidden; background: var(--white); }
  .flyer {
    position: relative;
    width: 849px;
    height: 1200px;
    overflow: hidden;
    background: radial-gradient(ellipse at 55% 45%, var(--red-bright) 0%, var(--red-mid) 45%, var(--red-deep) 100%);
    font-family: "Lora", Georgia, serif;
    color: var(--white);
  }
  .ornaments {
    position: absolute; left: 0; top: 0; width: 420px; height: 270px;
    background:
      radial-gradient(circle at 70% 25%, rgba(246,208,110,.85) 0 9%, transparent 10%),
      radial-gradient(circle at 30% 45%, rgba(230,181,60,.8) 0 14%, transparent 15%),
      radial-gradient(circle at 12% 12%, rgba(200,140,40,.7) 0 10%, transparent 11%),
      radial-gradient(ellipse at 30% 30%, rgba(180,110,30,.35), transparent 70%);
  }
  .snowflakes {
    position: absolute; left: 0; top: 640px; width: 849px; height: 240px;
    background:
      radial-gradient(circle at 15% 40%, rgba(255,255,255,.55) 0 4%, transparent 5%),
      radial-gradient(circle at 40% 55%, rgba(255,255,255,.45) 0 3%, transparent 4%),
      radial-gradient(circle at 70% 30%, rgba(255,255,255,.5) 0 5%, transparent 6%),
      radial-gradient(circle at 88% 60%, rgba(255,255,255,.4) 0 3%, transparent 4%);
  }
  .snowbank {
    position: absolute; left: 0; top: 820px; width: 849px; height: 200px;
    background: linear-gradient(180deg, rgba(255,255,255,0) 0%, rgba(255,255,255,.75) 45%, var(--white) 75%);
  }
  .base { position: absolute; left: 0; top: 1000px; width: 849px; height: 200px; background: var(--white); }

  .tickets { position: absolute; right: 16px; top: 28px; width: 290px; text-align: center; }
  .tickets__lead { font-size: 25px; font-weight: 700; line-height: 1.15; }
  .tickets__prices { font-size: 33px; font-weight: 700; line-height: 1.12; margin-top: 4px; }
  .tickets__note { font-size: 14px; line-height: 1.3; margin-top: 10px; }

  .title {
    position: absolute; left: 36px; top: 350px; width: 215px; text-align: center;
    font-family: "Stardos Stencil", "Courier New", monospace; font-weight: 700;
    font-size: 74px; line-height: 126px; letter-spacing: 0;
  }

  .event-box {
    position: absolute; left: 268px; width: 552px;
    border: 2px solid var(--white); text-align: center;
    font-variant: small-caps; font-size: 27px; line-height: 1.2; letter-spacing: .5px;
  }
  .event-box--sat { top: 418px; padding: 6px 0; }
  .event-box--sun { top: 482px; padding: 6px 0; }
  .event-box--venue { top: 546px; padding: 6px 0; line-height: 1.15; }

  .brand { position: absolute; left: 18px; top: 1048px; width: 400px; color: var(--purple); display: flex; align-items: center; gap: 12px; }
  .brand__mark { width: 22px; height: 22px; border-radius: 50%; background: var(--purple); flex: none; }
  .brand__name { font-size: 40px; font-weight: 600; line-height: 1; }
  .staff { position: absolute; left: 18px; top: 1115px; width: 400px; color: var(--purple); font-size: 15px; font-weight: 700; line-height: 1.35; }

  .program { position: absolute; left: 425px; top: 955px; width: 400px; text-align: center; color: var(--ink); font-size: 17px; line-height: 1.35; }
  .program strong { font-weight: 700; }

  .footnote { position: absolute; left: 18px; top: 1172px; width: 813px; color: var(--purple); font-size: 11px; font-style: italic; }
</style>
</head>
<body>
<main class="flyer">
  <div class="ornaments" role="img" aria-label="Gold star ornaments and baubles hanging from the top corner"></div>
  <div class="snowflakes" role="img" aria-label="Scattered white snowflakes"></div>
  <div class="snowbank" role="img" aria-label="White snowdrift with snowflakes"></div>
  <div class="base"></div>

  <section class="tickets">
    <p class="tickets__lead">Tickets available online<br>and at the door:</p>
    <p class="tickets__prices">General $20<br>Seniors $15<br>Students $10</p>
    <p class="tickets__note">Complimentary childcare<br>provided at both performances.<br>www.evergreenchorale-abq.org</p>
  </section>

  <h1 class="title">LOVE<br>&amp;<br>JOY</h1>

  <p class="event-box event-box--sat">Saturday, December 1 at 5:00pm</p>
  <p class="event-box event-box--sun">Sunday, December 2 at 3:00pm</p>
  <p class="event-box event-box--venue">St. Mark's Community<br>Church 1480 Mesa Street<br>NE Albuquerque</p>

  <div class="brand"><span class="brand__mark"></span><span class="brand__name">Evergreen Chorale</span></div>
  <p class="staff">Daniel Hale, Artistic Director<br>Rosa Linden Vega, Executive Director</p>

  <section class="program">
    <p>Daniel Hale, Artistic Director</p>
    <p>Join the singers of Evergreen Chorale as we perform carols, chorales, and other joyful and poignant music of the season!</p>
    <p><strong>With Special Guests</strong></p>
    <p>The Choirs of Harmon Middle School</p>
    <p><strong>Owen Tate, Director</strong></p>
  </section>

  <p class="footnote">Evergreen Chorale is a 501(c)3 nonprofit organization, and an Ensemble-in-Residence at St. Mark's Community Church.</p>
</main>
</body>
</html>
```